Pyramide TAGESFLUSS
Zielgruppe
Tobias Rahnfeld ist... Der Mann mit dem roten Stirnband (www.tobias-rahnfeld.com)
Videoinfo (BITTE UNBEDINGT ANSCHAUEN) unter:
http://www.clipvora.com/watch?v=pQ7mwe3tz8a
Er ist die Personifizierung eines eigenverantwortlichen und selbstbestimmten Lebens. Seit mehr als 15 Jahren beschäftigt er sich mit der Psychologie des Erfolgs und den Gesetzen des Lebens. Er entwickelte die Pyramide TAGESFLUSS und ist Urheber des Konzeptes SONNENKREIS WACHSEN.
Einzigartigkeit hat Tobias Rahnfeld schon früh erfahren. Im Alter von 16 war er nicht nur der jüngste Spieler in der Korbball-Oberklasse, sondern neun Jahre später auch einer der jüngsten Korbball-Oberklasse-Cheftrainer in der Geschichte dieses Sports. Er hat mit Jens Haverkamp zusammen gespielt, zwei Europameisterschaften für die deutsche Junioren-Nationalmannschaft absolviert und eine Europameisterschaft als Trainer gecoacht.
Parallel zu seiner Trainerkarriere hat Rahnfeld das BWL-Studium erfolgreich abgeschlossen. Darüber hinaus konnte er von Weltklasse-Nationaltrainern wie Uwe Leitgeber (Deutschland) oder Todd Wanamaker (USA) lernen, was Führungsstärke und -intelligenz bedeutet.
+++ Welche Produkte bieten wir an? -> Seminare, Vorträge und Bücher/Hörbücher +++
Tobias Rahnfeld steht für Erfolg, Glück und Erfüllung. Heute gibt er seine Expertise als gefragter Referent national und international an viele Menschen in Unternehmen aller Branchen weiter. Seine Seminarreihe SONNENKREIS WACHSEN mit den Events DER MUT, DEINEN WEG ZU GEHEN (www.tobias-rahnfeld.com/dermut), TATENDRANG Das Denken auf Ziele ausrichten (http://www.tobias-rahnfeld.com/events-tatendrang) und INNENSTÄRKE Freude und Sinn gestalten (www.tobias-rahnfeld.com/innenstaerke) hat sich in der Spitze der Persönlichkeitsentwicklung etabliert. Sie vermittelt Privatpersonen aller Altersklassen das Wissen, die mentalen Fähigkeiten und umsetzbaren Stra..
Aufgabenstellung
Es geht darum, die bereits bestehende Pyramide (zu sehen unter: http://www.tobias-rahnfeld.com/de/konzept) in eine neue "Form" zu bringen, die unserer gesamten CI/CD besser entspricht als die jetzige Variante. Sie muss/darf nicht wirklich ein Kunstwerk werden, sollte jedoch insgesamt dem Stil unseres Auftrittes entsprechen. Sie wird sowohl in Vorträgen und Seminaren an der Leinwand vor etlichen Leuten zu sehen sein, als auch auf der Website und in unseren Kommunikationsmaterialien Verwendung finden.
Zu den Reglern:
Modern - sie darf nicht zu modern sein, sollte jedoch auch nicht zu klassisch daher kommen. Die Zielgruppe sind Menschen von jung bis alt. Es geht hier nicht darum, eine spezielle Zielgruppe anzusprechen, sondern eher, eine einprägsame und schnell verständliche sowie übersichtliche Pyramide zu gestallten.
Exklusiv - kein Kommentar dazu. Eher im Mittelfeld.
Verspielt - weder noch. Zielgruppe ist weit gefasst, von daher muss auch die Pyramide vielen Menschen gefallen und sie muss ansprechend dargestellt werden.
Einfarbig: Es müssen die CI-Farben verwendet werden. Wichtig!
LAB: 38 63 37 - CMYK: 020 100 085 010 - RGB: 184 0 34 - HEX: B80022
Typo: Helvetica Neue LT Std

```html
<!DOCTYPE html>
<html lang="de">
<head>
<meta charset="utf-8">
<title>Pyramide TAGESFLUSS</title>
<link href="https://fonts.googleapis.com/css2?family=Inter:wght@300;400;600;800&display=swap" rel="stylesheet">
<style>
  :root {
    --brand-red: #b71729;
    --tier-face: #e6e1d6;
    --tier-divider: #c9c3b7;
    --ink: #111111;
    --paper: #ffffff;
  }
  html, body {
    margin: 0;
    padding: 0;
    width: 1200px;
    height: 920px;
    overflow: hidden;
    background: var(--paper);
  }
  .canvas {
    width: 1200px;
    height: 920px;
    position: relative;
    font-family: "Inter", "Helvetica Neue", Arial, sans-serif;
  }
  .pyramid-graphic {
    position: absolute;
    top: 10px;
    left: 0;
    width: 1200px;
    height: 900px;
  }
  .title-light { font-weight: 300; fill: var(--ink); font-size: 56px; letter-spacing: -1px; }
  .title-bold { font-weight: 800; fill: var(--brand-red); letter-spacing: 0; }
  .level-label { font-size: 24px; font-weight: 400; fill: var(--ink); }
  .level-label--active { fill: var(--brand-red); }
  .level-rule { stroke: var(--ink); stroke-width: 2; }
  .level-rule--active { stroke: var(--brand-red); }
  .tier-face { fill: var(--tier-face); }
  .tier-divider { stroke: var(--tier-divider); stroke-width: 1.5; }
  .tier-term { font-size: 16px; font-weight: 400; fill: var(--ink); text-anchor: middle; }
  .tier-term--apex { font-size: 32px; }
  .tier-term--highlight { font-weight: 600; font-size: 15px; fill: var(--paper); }
  .highlight-box { fill: var(--brand-red); }
  .foundation-face { fill: var(--brand-red); }
  .foundation-text { font-size: 53px; font-weight: 800; fill: var(--paper); text-anchor: middle; letter-spacing: 1px; }
</style>
</head>
<body>
<main class="canvas">
  <svg class="pyramid-graphic" viewBox="0 0 1280 960" xmlns="http://www.w3.org/2000/svg" role="img" aria-label="Pyramide TAGESFLUSS mit sechs Ebenen auf dem Fundament Eigenverantwortung">
    <text x="340" y="97" class="title-light">PYRAMIDE <tspan class="title-bold">TAGESFLUSS</tspan></text>

    <g class="level-labels">
      <text x="42" y="286" class="level-label">SINNEBENE</text>
      <line x1="42" y1="295" x2="617" y2="295" class="level-rule"/>
      <text x="44" y="372" class="level-label">SOZIALEBENE</text>
      <line x1="44" y1="382" x2="560" y2="382" class="level-rule"/>
      <text x="44" y="461" class="level-label">DEFINITIONSEBENE</text>
      <line x1="44" y1="472" x2="500" y2="472" class="level-rule"/>
      <text x="44" y="551" class="level-label level-label--active">WISSENSEBENE</text>
      <line x1="44" y1="561" x2="438" y2="561" class="level-rule level-rule--active"/>
      <text x="44" y="638" class="level-label">HANDLUNGSEBENE</text>
      <line x1="44" y1="649" x2="381" y2="649" class="level-rule"/>
      <text x="44" y="731" class="level-label">MENTALEBENE</text>
      <line x1="44" y1="740" x2="319" y2="740" class="level-rule"/>
    </g>

    <g class="pyramid-tiers">
      <polygon class="tier-face" points="732,158 813.5,287 641.8,287"/>
      <text x="727" y="266" class="tier-term tier-term--apex">SINN</text>

      <polygon class="tier-face" points="637.6,293 817.3,293 869.8,376 579.5,376"/>
      <line x1="721" y1="313" x2="721" y2="358" class="tier-divider"/>
      <text x="670" y="344" class="tier-term">UMFELD</text>
      <text x="773" y="344" class="tier-term">UMGANG</text>

      <polygon class="tier-face" points="575.3,382 873.6,382 926,465 517.3,465"/>
      <line x1="646" y1="402" x2="646" y2="448" class="tier-divider"/>
      <line x1="788" y1="402" x2="788" y2="448" class="tier-divider"/>
      <text x="599" y="433" class="tier-term">WERTE</text>
      <text x="713" y="433" class="tier-term">SELBSTBILD</text>
      <text x="840" y="433" class="tier-term">REGELN</text>

      <polygon class="tier-face" points="513.1,471 929.8,471 981.6,553 455.7,553"/>
      <line x1="878" y1="491" x2="878" y2="537" class="tier-divider"/>
      <rect class="highlight-box" x="573" y="483" width="160" height="60"/>
      <text x="530" y="524" class="tier-term">BERUF</text>
      <text x="653" y="518" class="tier-term tier-term--highlight">PARTNERSCHAFT</text>
      <text x="812" y="523" class="tier-term">GESUNDHEIT</text>
      <text x="915" y="523" class="tier-term">GELD</text>

      <polygon class="tier-face" points="450.9,560 986.1,560 1038.5,643 392.8,643"/>
      <line x1="534" y1="583" x2="534" y2="628" class="tier-divider"/>
      <line x1="675" y1="583" x2="675" y2="628" class="tier-divider"/>
      <line x1="752" y1="583" x2="752" y2="628" class="tier-divider"/>
      <line x1="880" y1="583" x2="880" y2="628" class="tier-divider"/>
      <text x="479" y="613" class="tier-term">DISZIPLIN</text>
      <text x="602" y="613" class="tier-term">PRIORITÄTEN</text>
      <text x="713" y="613" class="tier-term">ZIELE</text>
      <text x="813" y="613" class="tier-term">AUSDAUER</text>
      <text x="935" y="613" class="tier-term">NEUGIER</text>

      <polygon class="tier-face" points="388.6,649 1042.3,649 1094.8,732 330.5,732"/>
      <line x1="485" y1="671" x2="485" y2="716" class="tier-divider"/>
      <line x1="601" y1="671" x2="601" y2="716" class="tier-divider"/>
      <line x1="723" y1="671" x2="723" y2="716" class="tier-divider"/>
      <line x1="848" y1="671" x2="848" y2="716" class="tier-divider"/>
      <line x1="921" y1="671" x2="921" y2="716" class="tier-divider"/>
      <text x="420" y="701" class="tier-term">EMOTIONEN</text>
      <text x="543" y="700" class="tier-term">GEDANKEN</text>
      <text x="665" y="691" class="tier-term">SELBST-</text>
      <text x="665" y="711" class="tier-term">VERTRAUEN</text>
      <text x="785" y="691" class="tier-term">ÜBER-</text>
      <text x="785" y="711" class="tier-term">ZEUGUNGEN</text>
      <text x="885" y="702" class="tier-term">FOKUS</text>
      <text x="992" y="702" class="tier-term">SPIRITUALITÄT</text>

      <polygon class="foundation-face" points="325.6,739 1099.2,739 1156.7,830 262,830"/>
      <text x="709" y="805" class="foundation-text">EIGENVERANTWORTUNG</text>
    </g>
  </svg>
</main>
</body>
</html>
```